Mindfulness School for Children -- Business Cards

We're looking for business cards for our school directors and owners. We're a mindfulness school for children called little compass. Attached are our logos/icons.

```html
<!DOCTYPE html>
<html lang="en">
<head>
<meta charset="utf-8">
<title>little compass — Business Cards</title>
<link href="https://fonts.googleapis.com/css2?family=Arimo:wght@400;500&display=swap" rel="stylesheet">
<style>
  :root {
    --backdrop: #cfcfcf;
    --card-white: #ffffff;
    --teal: #3fa3b8;
    --green: #5fae92;
    --rule: #4fb1c9;
    --ink: #3a3a3a;
    --icon: #6fb59a;
    --back-top: #74c3d6;
    --back-bottom: #5fa98d;
    --edge: #4fb3cf;
  }
  * { margin: 0; padding: 0; box-sizing: border-box; }
  html, body {
    width: 1200px; height: 800px; overflow: hidden;
    background: var(--backdrop);
    font-family: "Arimo", Arial, sans-serif;
  }
  .sheet {
    position: relative; width: 1200px; height: 800px;
    display: flex; align-items: center; justify-content: center; gap: 50px;
  }
  .card {
    position: relative; width: 520px; height: 297px;
    border-bottom: 2px solid var(--edge);
    box-shadow: 0 6px 18px rgba(0,0,0,0.18);
    overflow: hidden;
  }
  /* front */
  .card-front { background: var(--card-white); }
  .brand {
    position: absolute; top: 34px; right: 36px;
    display: flex; align-items: center; gap: 10px;
  }
  .brand-dot { width: 16px; height: 16px; border-radius: 50%; background: var(--teal); }
  .brand-name { font-size: 31px; font-weight: 400; color: var(--teal); letter-spacing: 0.5px; }
  .person { position: absolute; left: 36px; top: 110px; }
  .person-name { font-size: 25px; font-weight: 500; color: var(--green); }
  .person-name .surname { color: var(--teal); }
  .person-role { font-size: 14px; color: var(--ink); margin-top: 2px; }
  .divider {
    position: absolute; left: 36px; right: 70px; top: 168px;
    height: 1px; background: var(--rule);
  }
  .contacts { position: absolute; left: 36px; top: 184px; list-style: none; }
  .contacts li {
    display: flex; align-items: center; gap: 8px;
    font-size: 14px; color: var(--ink); line-height: 22px;
  }
  .contacts svg { width: 13px; height: 13px; flex: none; }
  .address {
    position: absolute; right: 40px; top: 184px;
    font-size: 14px; color: var(--ink); line-height: 22px; text-align: right;
  }
  /* back */
  .card-back { background: linear-gradient(160deg, var(--back-top) 0%, var(--back-bottom) 100%); }
  .pattern-field {
    position: absolute; inset: 0;
    background: linear-gradient(160deg, #7ccbd6 0%, #6cb9a6 55%, #5da487 100%);
  }
  .back-brand {
    position: absolute; right: 38px; bottom: 70px;
    display: flex; align-items: center; gap: 12px;
  }
  .back-brand .brand-dot { background: #ffffff; width: 18px; height: 18px; }
  .back-brand .brand-name { color: #ffffff; font-size: 40px; }
</style>
</head>
<body>
<main class="sheet">
  <section class="card card-front" aria-label="Business card front">
    <div class="brand">
      <span class="brand-dot"></span>
      <span class="brand-name">little compass</span>
    </div>
    <div class="person">
      <p class="person-name">Daniel <span class="surname">Hartley</span></p>
      <p class="person-role">Managing Director</p>
    </div>
    <div class="divider"></div>
    <ul class="contacts">
      <li>
        <svg viewBox="0 0 16 16"><path fill="var(--icon)" d="M4 1l3 3-2 2c1 2 3 4 5 5l2-2 3 3-2 3C7 15 1 9 1 4z"/></svg>
        044-987 654 321
      </li>
      <li>
        <svg viewBox="0 0 16 16"><rect x="1" y="3" width="14" height="10" fill="var(--icon)"/><path d="M1 3l7 6 7-6" fill="none" stroke="#fff" stroke-width="1.3"/></svg>
        hello@littlecompass.org
      </li>
      <li>
        <svg viewBox="0 0 16 16"><circle cx="8" cy="8" r="7" fill="var(--icon)"/><path d="M1 8h14M8 1c-3 4-3 10 0 14M8 1c3 4 3 10 0 14" fill="none" stroke="#fff" stroke-width="1"/></svg>
        www.littlecompass.org
      </li>
    </ul>
    <address class="address" style="font-style:normal">
      27, Willow Lane<br>45120, Fernvale
    </address>
  </section>

  <section class="card card-back" aria-label="Business card back">
    <div class="pattern-field" role="img" aria-label="Repeating embossed flower pattern in soft teal and green"></div>
    <div class="back-brand">
      <span class="brand-dot"></span>
      <span class="brand-name">little compass</span>
    </div>
  </section>
</main>
</body>
</html>
```